Logo needed for business card

Velquist Pty Ltd is in the business of healthcare and ecommerce.

We own and manage pharmacies and online health ecomerce sites.

We provide ecommerce consultants for companies looking for an ecommerce business startegy.

Think of it as the umbrella under which several healthcare brands may sit.

When I think of Velquist, I visulaise slick black/metalic colours, so please stay away from the common blue and green colours that seem to be so popular in this field.

Target Market(s)

CEOs and COOs

Industry/Entity Type

Healthcare

Contact Information for Business Card

Tessa Lindqvist
Director
Velquist Pty Ltd
4/362 Fennick Pde
Brellton, NSW 2148

Requirements
Must have
• Design must have scope to be implemented on the company's website and letterheads etc.

```html
<!DOCTYPE html>
<html lang="en">
<head>
<meta charset="utf-8">
<title>Velquist Pty Ltd — Business Card</title>
<link rel="stylesheet" href="https://fonts.googleapis.com/css2?family=Ubuntu:wght@300;400&display=swap">
<style>
  :root {
    --page-bg: #d9d9d9;
    --card-bg: #0b0b0b;
    --brand-white: #f2f2f2;
    --name-grey: #5c5c5c;
    --detail-grey: #8a8a8a;
    --icon-grey: #6e6e6e;
    --emblem-grey: #262626;
  }
  * { margin: 0; padding: 0; box-sizing: border-box; }
  html, body {
    width: 1200px;
    height: 900px;
    overflow: hidden;
    background: var(--page-bg);
  }
  .business-card {
    position: absolute;
    left: 150px;
    top: 190px;
    width: 900px;
    height: 520px;
    background: var(--card-bg);
    overflow: hidden;
    font-family: "Ubuntu", sans-serif;
    box-shadow: 0 12px 30px rgba(0,0,0,0.25);
  }
  .brand {
    position: absolute;
    left: 37px;
    top: 44px;
    display: flex;
    align-items: center;
    gap: 38px;
  }
  .brand-dot {
    width: 74px;
    height: 74px;
    border-radius: 50%;
    background: var(--brand-white);
  }
  .brand-name {
    color: var(--brand-white);
    font-weight: 300;
    font-size: 34px;
  }
  .card-emblem {
    position: absolute;
    left: 471px;
    top: 88px;
    width: 414px;
    height: 414px;
    border-radius: 50%;
    background: var(--emblem-grey);
  }
  .person {
    position: absolute;
    left: 50px;
    top: 186px;
  }
  .person-name {
    color: var(--name-grey);
    font-weight: 400;
    font-size: 40px;
    line-height: 1;
  }
  .person-role {
    color: var(--name-grey);
    font-weight: 300;
    font-size: 21px;
    margin-top: 2px;
  }
  .contact-list {
    position: absolute;
    left: 56px;
    top: 300px;
    list-style: none;
  }
  .contact-item {
    display: flex;
    align-items: center;
    height: 66px;
    color: var(--detail-grey);
    font-weight: 300;
    font-size: 20px;
  }
  .contact-icon {
    width: 28px;
    height: 28px;
    margin-right: 36px;
    fill: var(--icon-grey);
  }
</style>
</head>
<body>
  <section class="business-card" aria-label="Velquist Pty Ltd business card">
    <div class="card-emblem" role="img" aria-label="Large faint brand emblem"></div>

    <header class="brand">
      <span class="brand-dot"></span>
      <span class="brand-name">Velquist Pty Ltd</span>
    </header>

    <div class="person">
      <p class="person-name">Tessa Lindqvist</p>
      <p class="person-role">Director</p>
    </div>

    <ul class="contact-list">
      <li class="contact-item">
        <svg class="contact-icon" viewBox="0 0 24 24" aria-hidden="true">
          <path d="M6.6 10.8a15.1 15.1 0 0 0 6.6 6.6l2.2-2.2c.3-.3.7-.4 1-.2 1.1.4 2.3.6 3.6.6.6 0 1 .4 1 1V20c0 .6-.4 1-1 1C10.6 21 3 13.4 3 4c0-.6.4-1 1-1h3.5c.6 0 1 .4 1 1 0 1.3.2 2.5.6 3.6.1.3 0 .7-.2 1z"/>
        </svg>
        <span class="contact-text">xxx-xxx-xxxx</span>
      </li>
      <li class="contact-item">
        <svg class="contact-icon" viewBox="0 0 24 24" aria-hidden="true">
          <path d="M3 5h18v14H3z M4.5 6.5 12 12l7.5-5.5" />
          <path d="M3 5h18v2l-9 6-9-6z" fill="#0b0b0b" opacity="0.35"/>
        </svg>
        <span class="contact-text">xxxxxx@xxxxxxx.com</span>
      </li>
      <li class="contact-item">
        <svg class="contact-icon" viewBox="0 0 24 24" aria-hidden="true">
          <path d="M12 2a7 7 0 0 0-7 7c0 5.2 7 13 7 13s7-7.8 7-13a7 7 0 0 0-7-7zm0 9.5A2.5 2.5 0 1 1 12 6.5a2.5 2.5 0 0 1 0 5z"/>
        </svg>
        <span class="contact-text">4/362 Fennick Pde Brellton, NSW 2148</span>
      </li>
    </ul>
  </section>
</body>
</html>
```